Business Card Design REAL ESTATE SALES PLEASE DESIGN MY CARD 2COLOR CARD WITH RED AS THE DOMINANT

FERNHOLM REALTY
TorLPA Lic# 04738216
RAFAEL " RAFE " MORTON Tel 555 218-3396
TorLPA Lic# 02864057 Fax 555 218-3740
Email: rafe@rafemortonhomes.net Cell 555 902-4481
47530 WREN TERRACE UNION CITY, CA 94312

RAFAEL " RAFE " MORTON
TEL: 555 218-3396 FAX 555 218-3740
Address: 47530 Wren Terrace Union City , CA
EMAIL ADDRESS: rafe@rafemortonhomes.net

```html
<!DOCTYPE html>
<html lang="en">
<head>
<meta charset="utf-8">
<title>Fernholm Realty — Business Card</title>
<link rel="stylesheet" href="https://fonts.googleapis.com/css2?family=Open+Sans:wght@400;600;700&display=swap">
<style>
  :root {
    --backdrop: #3b3b3d;
    --card: #0d0d0e;
    --card-edge: #1c1c1e;
    --red: #d4201f;
    --white: #f2f2f2;
    --silver: #c9c9c9;
  }
  * { margin: 0; padding: 0; box-sizing: border-box; }
  html, body { width: 1200px; height: 900px; overflow: hidden; }
  body {
    background: var(--backdrop);
    font-family: "Open Sans", Arial, sans-serif;
    position: relative;
  }
  .card {
    position: absolute;
    top: 307px;
    width: 500px;
    height: 286px;
    background: var(--card);
    border: 1px solid var(--card-edge);
    border-radius: 20px;
    box-shadow: 0 10px 28px rgba(0,0,0,.45);
  }
  .card--front { left: 80px; }
  .card--back { left: 620px; }

  .brand {
    position: absolute;
    display: flex;
    align-items: center;
    gap: 12px;
  }
  .brand__dot {
    width: 26px; height: 26px;
    border-radius: 50%;
    background: var(--red);
    flex: none;
  }
  .brand__name {
    font-weight: 600;
    color: var(--silver);
    letter-spacing: .5px;
  }
  .card--front .brand { left: 40px; top: 128px; }
  .card--front .brand__name { font-size: 19px; }
  .card--back .brand { left: 0; right: 0; top: 126px; justify-content: center; }
  .card--back .brand__name { font-size: 28px; }

  .details {
    position: absolute;
    left: 268px;
    top: 38px;
    color: var(--white);
    font-size: 12.5px;
    line-height: 1.35;
  }
  .details__name {
    font-size: 15px;
    font-weight: 700;
    color: var(--red);
    margin-bottom: 8px;
  }
  .details__name .nickname { color: var(--white); }
  .details__address { margin-bottom: 6px; }
  .licence { color: var(--red); font-weight: 600; }
  .licence .number { color: var(--white); font-weight: 400; }
  .contacts { list-style: none; margin-top: 12px; }
  .contacts li { display: flex; align-items: center; gap: 9px; height: 17px; }
  .contacts svg { width: 10px; height: 10px; fill: var(--red); flex: none; }
</style>
</head>
<body>

<section class="card card--front" aria-label="Card front">
  <div class="brand">
    <span class="brand__dot"></span>
    <span class="brand__name">FERNHOLM REALTY</span>
  </div>

  <div class="details">
    <p class="details__name">RAFAEL <span class="nickname">" RAFE "</span> MORTON</p>
    <p class="details__address">47530 Wren Terrace<br>Union City, CA 94312</p>
    <p class="licence">TorLPA Lic# <span class="number">02864057</span></p>
    <p class="licence">TorLPA Lic# <span class="number">04738216</span></p>
    <ul class="contacts">
      <li>
        <svg viewBox="0 0 10 10" aria-label="Telephone"><path d="M2 0.5 L3.6 2.6 L2.7 3.6 Q4 6 6.4 7.3 L7.4 6.4 L9.5 8 L8.4 9.5 Q4.5 9.5 0.5 1.6 Z"/></svg>
        <span>555 218-3396</span>
      </li>
      <li>
        <svg viewBox="0 0 10 10" aria-label="Cell"><path d="M2.5 0 H7.5 V10 H2.5 Z M3.4 1.2 V7.8 H6.6 V1.2 Z"/></svg>
        <span>555 902-4481</span>
      </li>
      <li>
        <svg viewBox="0 0 10 10" aria-label="Fax"><path d="M2.5 0 H7.5 V3 H2.5 Z M0.5 3.5 H9.5 V8 H8 V10 H2 V8 H0.5 Z M3 6.5 V9 H7 V6.5 Z"/></svg>
        <span>555 218-3740</span>
      </li>
      <li>
        <svg viewBox="0 0 10 10" aria-label="Email"><path d="M0 1.5 H10 V8.5 H0 Z M0.8 2.2 L5 5.4 L9.2 2.2 Z"/></svg>
        <span>rafe@rafemortonhomes.net</span>
      </li>
    </ul>
  </div>
</section>

<section class="card card--back" aria-label="Card back">
  <div class="brand">
    <span class="brand__dot"></span>
    <span class="brand__name">FERNHOLM REALTY</span>
  </div>
</section>

</body>
</html>
```